Building company buisness cards

We are looking for a sharp modern new look for our business cards.We are a New Zealand based company that specialises in house and land packages.We have attached a photo of the current logo and would like to see if it can be improved somehow if needed.We are open to any colours but we have chosen Black and White at this stage. Feel free to change the font and make the logo smarter looking.Play with the colours and see what looks best.We want a card that looks so good know one will want to throw it away!

Target Market(s)

Building profesonals, home buyers

Industry/Entity Type

Building

Contact Information for Business Card

Derek Haskins
0274930268
derekh@stonerange.co.nz

Font styles to use
Serif
Sans Serif

Colors

Designer to choose colors to be used in the design.

Requirements
Must have
• Just the logo on one side and details on the other
• Clean simple looking card
Nice to have
• Round corners and detail like raised or spot UV
• Something that stands out
Should not have
• To title needed, Director etc

```html
<!DOCTYPE html>
<html lang="en">
<head>
<meta charset="utf-8">
<title>Stonerange Business Cards</title>
<link rel="stylesheet" href="https://fonts.googleapis.com/css2?family=Open+Sans:wght@400;700&family=Playfair+Display:wght@700&display=swap">
<style>
  :root {
    --backdrop: #2b2b2d;
    --card-black: #161617;
    --card-white: #ffffff;
    --ink: #111111;
    --ink-soft: #6a6a6a;
    --silver: #d9d9d9;
    --silver-dim: #a9a9a9;
  }
  * { margin: 0; padding: 0; box-sizing: border-box; }
  html, body {
    width: 1200px;
    height: 885px;
    overflow: hidden;
    background: var(--backdrop);
  }
  .sheet {
    width: 1200px;
    height: 885px;
    display: flex;
    flex-direction: column;
    align-items: center;
    justify-content: center;
    gap: 56px;
  }
  .card {
    position: relative;
    width: 600px;
    height: 343px;
    border-radius: 22px;
    box-shadow: 0 14px 30px rgba(0,0,0,0.45);
  }
  /* Logo side */
  .card--logo {
    background: linear-gradient(160deg, #222224 0%, var(--card-black) 60%);
  }
  .card--logo .mark {
    position: absolute;
    left: 50%;
    top: 52px;
    width: 168px;
    height: 168px;
    margin-left: -84px;
  }
  .card--logo .site {
    position: absolute;
    left: 0;
    right: 0;
    bottom: 62px;
    text-align: center;
    font-family: "Open Sans", sans-serif;
    font-size: 13px;
    letter-spacing: 6px;
    color: var(--silver);
  }
  /* Details side */
  .card--details {
    background: var(--card-white);
  }
  .brand {
    position: absolute;
    top: 34px;
    right: 34px;
    display: flex;
    align-items: center;
    gap: 8px;
  }
  .brand__name {
    font-family: "Playfair Display", serif;
    font-weight: 700;
    font-size: 40px;
    line-height: 1;
    color: var(--ink);
  }
  .brand__dot {
    width: 34px;
    height: 34px;
    border: 2px solid var(--ink);
    border-radius: 50%;
  }
  .card--details .site {
    position: absolute;
    right: 36px;
    top: 150px;
    font-family: "Open Sans", sans-serif;
    font-size: 13px;
    color: var(--ink-soft);
  }
  .card--details .site strong { color: var(--ink); font-weight: 700; }
  .contact {
    position: absolute;
    left: 40px;
    bottom: 38px;
    font-family: "Open Sans", sans-serif;
    color: var(--ink);
  }
  .contact__name {
    font-size: 18px;
    font-weight: 700;
    margin-bottom: 10px;
  }
  .contact__line {
    font-size: 13px;
    line-height: 1.45;
    color: var(--ink-soft);
  }
  .contact__line b { color: var(--ink); font-weight: 700; }
</style>
</head>
<body>
<main class="sheet">
  <section class="card card--logo">
    <svg class="mark" viewBox="0 0 168 168" aria-hidden="true">
      <defs>
        <linearGradient id="foil" x1="0" y1="0" x2="1" y2="1">
          <stop offset="0" stop-color="#f2f2f2"/>
          <stop offset="0.5" stop-color="#9c9c9c"/>
          <stop offset="1" stop-color="#e6e6e6"/>
        </linearGradient>
      </defs>
      <circle cx="84" cy="84" r="80" fill="none" stroke="url(#foil)" stroke-width="4"/>
    </svg>
    <p class="site">www.stonerange.co.nz</p>
  </section>

  <section class="card card--details">
    <div class="brand">
      <span class="brand__name">Stonerange</span>
      <span class="brand__dot"></span>
    </div>
    <p class="site">www.<strong>stonerange</strong>.co.nz</p>
    <div class="contact">
      <p class="contact__name">Derek Haskins</p>
      <p class="contact__line"><b>Phone:</b> 0274930268</p>
      <p class="contact__line"><b>Email:</b> derekh@stonerange.co.nz</p>
    </div>
  </section>
</main>
</body>
</html>
```